Online eyewear company needs a couple Sign-In and Product Review page designs

We sell prescription glasses starting at $99 with Free Shipping. We have over 300 different styles and colors.Our website is under construction and we need an amazing Sign-In and Product Review Pages to help finish things off. Our brand is called VESKA and our website is called VESKAEYEWEAR.COM.

We need 5 simple sign-in and product review pages to help finish our website. Sample pages attached

We need the pages to go in order

Quick Checkout review
Sign-In
Prescription
Shipping & Payment
Final Review

Target Market(s)

20-50 that wears glasses

Industry/Entity Type

Eyewear

Colors
ffffff
919191
eaeaea
d3d3d3
dddddd
b7b7b7
000000
3176b5

Requirements
Must have
• Simple, creative, original. Must not be exactly like the photos attached. They're just templete of our casual, simple style.
• We need the pages to go in order
• Quick Checkout review
• Sign-In
• Prescription
• Shipping & Payment
• Final Review
Should not have
• Must not look exactly like the photos attached.

```html
<!DOCTYPE html>
<html lang="en">
<head>
<meta charset="utf-8">
<title>VESKA — Your Cart</title>
<link rel="stylesheet" href="https://fonts.googleapis.com/css2?family=Open+Sans:ital,wght@0,300;0,400;0,600;0,700;1,400;1,600&family=Lato:wght@400;700&display=swap">
<style>
:root{
  --white:#ffffff;
  --grey-mid:#919191;
  --grey-light:#eaeaea;
  --grey-line:#d3d3d3;
  --grey-soft:#dddddd;
  --grey-dim:#b7b7b7;
  --black:#000000;
  --brand-blue:#3176b5;
  --checkout-blue:#1f5fa3;
  --signup-blue:#00a8ec;
  --footer:#262626;
  --text:#333333;
  --overlay:rgba(0,0,0,.62);
}
*{box-sizing:border-box;margin:0;padding:0}
html,body{width:1200px;height:1015px;overflow:hidden}
body{position:relative;background:var(--grey-light);font-family:"Open Sans",sans-serif;color:var(--text)}
.abs{position:absolute}
.topbar{left:0;top:0;width:1200px;height:30px;background:#e9e9e9;font-family:"Lato",sans-serif;font-size:10px;text-align:center;line-height:30px;color:#111}
.header{left:0;top:30px;width:1200px;height:58px;background:#dadada;border-bottom:1px solid #ccc}
.brand{left:90px;top:41px;font-family:"Lato",sans-serif;font-size:22px;letter-spacing:4px;color:#111}
.nav{top:51px;font-family:"Lato",sans-serif;font-size:13px;color:#222}
.util{top:54px;font-family:"Lato",sans-serif;font-size:11.5px;color:#555}
.cart-btn{left:1150px;top:11px;width:34px;height:35px;background:var(--white);border-radius:6px;box-shadow:0 1px 3px rgba(0,0,0,.4)}
.cart-badge{left:1140px;top:3px;width:16px;height:16px;border-radius:50%;background:#b0106e;color:#fff;font-size:8px;text-align:center;line-height:16px}
.cart-title{left:250px;top:130px;font-size:16px;font-weight:300;color:#444}
.update-btn{left:870px;top:126px;width:80px;height:21px;background:var(--brand-blue);color:#fff;font-size:10.5px;text-align:center;line-height:21px}
.th{top:192px;font-size:10.5px;color:#444}
.rule{height:1px;background:var(--grey-line)}
.frame-photo{width:62px;height:50px;background:linear-gradient(135deg,#f2f2f2,#d8d8d8)}
.product-name{left:439px;top:245px;font-size:14px;color:#444}
.price{font-size:12.5px;color:#333;text-align:right;width:100px}
.summary{left:252px;top:590px;width:402px;height:124px;background:#dedede}
.summary-label{left:262px;top:595px;font-size:12px;font-style:italic;color:#555}
.sum-row{left:280px;width:346px;font-size:10px;color:#444;display:flex;justify-content:space-between}
.total-row{left:280px;top:684px;width:346px;font-size:15px;font-weight:600;color:#333;display:flex;justify-content:space-between}
.checkout-btn{left:672px;top:590px;width:282px;height:61px;background:var(--checkout-blue);color:#fff;font-size:16px;font-style:italic;text-align:center;line-height:61px}
.checkout-note{left:672px;top:661px;width:282px;text-align:center;font-size:7px;font-style:italic;color:#555}
.footer{left:0;top:809px;width:1200px;height:206px;background:var(--footer)}
.footer-brand{left:250px;top:848px;font-family:"Lato",sans-serif;font-size:38px;letter-spacing:7px;color:#fff}
.fcol{top:856px;font-size:12.5px;color:#e0e0e0}
.fcol h4{font-size:14px;font-weight:700;margin-bottom:9px;color:#fff}
.fcol p{line-height:22px;font-weight:300}
.overlay{left:0;top:0;width:1200px;height:1015px;background:var(--overlay)}
.modal{left:310px;top:263px;width:551px;height:350px;display:flex;box-shadow:0 0 12px rgba(0,0,0,.3)}
.modal-photo{width:232px;height:350px;background:linear-gradient(160deg,#c8c8c8,#a9a9a9 60%,#b5b5b5)}
.modal-form{flex:1;background:#ececec;position:relative;text-align:center}
.modal-close{left:864px;top:246px;width:16px;height:16px;background:#111;color:#fff;font-size:12px;line-height:15px;text-align:center;font-weight:700}
.form-title{position:absolute;left:0;width:100%;top:26px;font-size:21px;font-weight:700;color:#222;letter-spacing:.3px}
.form-sub{position:absolute;left:0;width:100%;top:53px;font-size:7.5px;color:#777}
.glasses{position:absolute;left:131px;top:76px}
.field{position:absolute;left:69px;width:198px;height:33px;background:#fff;font-size:10px;color:#bbb;text-align:left;padding-left:9px;line-height:33px}
.signup{position:absolute;left:69px;top:235px;width:198px;height:33px;background:var(--signup-blue);color:#fff;font-size:11px;font-weight:600;line-height:33px}
.terms{position:absolute;left:86px;width:164px;top:279px;font-size:7px;line-height:9.5px;color:#888;letter-spacing:-.2px}
.terms a{color:#5ab4e8;text-decoration:none}
.signin{position:absolute;left:0;width:100%;top:317px;font-size:7.5px;color:#666}
.signin b{color:#333}
</style>
</head>
<body>
<div class="abs topbar">FREE SHIPPING IN CONTINENTAL US</div>
<div class="abs header"></div>
<div class="abs brand">VESKA</div>
<div class="abs nav" style="left:281px">EYEGLASSES</div>
<div class="abs nav" style="left:374px">ORDER LENSES</div>
<svg class="abs" style="left:1028px;top:54px" width="12" height="12" viewBox="0 0 12 12"><circle cx="5" cy="5" r="4" fill="none" stroke="#777" stroke-width="1.6"/><line x1="8" y1="8" x2="11.5" y2="11.5" stroke="#777" stroke-width="1.8"/></svg>
<div class="abs util" style="left:1046px">SEARCH &nbsp;|&nbsp; HELP</div>
<div class="abs cart-btn"><svg width="34" height="35" viewBox="0 0 34 35"><path d="M8 15h18l-2.5 9h-13z" fill="#111"/><path d="M12 15l4-6M22 15l-4-6" stroke="#111" stroke-width="1.6" fill="none"/><circle cx="17" cy="19.5" r="1.3" fill="#fff"/></svg></div>
<div class="abs cart-badge">2</div>

<div class="abs cart-title">Your Cart (2)</div>
<div class="abs update-btn">Update Cart</div>
<div class="abs th" style="left:250px">Item</div>
<div class="abs th" style="left:688px">Price</div>
<div class="abs th" style="left:806px">Qty</div>
<div class="abs th" style="left:894px">SubTotal</div>
<div class="abs rule" style="left:250px;top:211px;width:706px"></div>

<div class="abs frame-photo" role="img" aria-label="Product photo of tortoise eyeglass frames" style="left:249px;top:266px"></div>
<div class="abs product-name">Halden</div>
<div class="abs price" style="left:834px;top:285px">$99.00</div>
<div class="abs rule" style="left:250px;top:372px;width:706px"></div>
<div class="abs frame-photo" role="img" aria-label="Product photo of tortoise eyeglass frames" style="left:249px;top:432px"></div>
<div class="abs price" style="left:834px;top:438px">$253.00</div>
<div class="abs rule" style="left:250px;top:530px;width:706px"></div>
<svg class="abs" style="left:886px;top:338px" width="48" height="18" viewBox="0 0 48 18"><path d="M2 16l2-5 9-9 3 3-9 9z" fill="none" stroke="#666"/><path d="M32 4h12M36 4V2h4v2M33 4l1 13h8l1-13" fill="none" stroke="#666"/></svg>
<svg class="abs" style="left:886px;top:499px" width="48" height="18" viewBox="0 0 48 18"><path d="M2 16l2-5 9-9 3 3-9 9z" fill="none" stroke="#666"/><path d="M32 4h12M36 4V2h4v2M33 4l1 13h8l1-13" fill="none" stroke="#666"/></svg>

<div class="abs summary"></div>
<div class="abs summary-label">Summary</div>
<div class="abs sum-row" style="top:628px"><span>SUB TOTAL</span><b>$352</b></div>
<div class="abs sum-row" style="top:653px"><span>SHIPPING FEE</span><b>FREE</b></div>
<div class="abs rule" style="left:278px;top:674px;width:358px;background:#999"></div>
<div class="abs total-row"><span>TOTAL</span><span>$352</span></div>
<div class="abs checkout-btn">Proceed to Checkout</div>
<div class="abs checkout-note">Free of Standard Shipping (CONTINENTAL US) and free return on all orders.</div>

<div class="abs footer"></div>
<div class="abs footer-brand">VESKA</div>
<div class="abs fcol" style="left:458px"><h4>PRODUCTS</h4><p>Men's Frames</p><p>Women's Frames</p><p>New Arrivals</p><p>Best Sellers</p><p>Featured Frames</p></div>
<div class="abs fcol" style="left:636px"><h4>ORDER</h4><p>Single Vision Lenses</p><p>Blue Light Blocking</p><p>Computer Lenses</p><p>High Index Lenses</p><p>Transition Lenses</p><p>Reading Lenses</p></div>
<div class="abs fcol" style="left:814px"><h4>INFORMATION</h4><p>Track Order</p><p>About Us</p><p>Contact Us</p><p>Returns</p><p>Warranty</p><p>FAQ</p></div>

<div class="abs overlay"></div>

<div class="abs modal-close">×</div>
<div class="abs modal">
  <div class="modal-photo" role="img" aria-label="Desk flat-lay with laptop, calculator, notepad, pen, glasses and coffee"></div>
  <div class="modal-form">
    <div class="form-title">LET'S GET YOU SETUP!</div>
    <div class="form-sub">Fill in this form to create an account.</div>
    <svg class="glasses" width="70" height="24" viewBox="0 0 70 24"><path d="M2 4h66M5 4c0 12 4 17 13 17s12-6 12-17M40 4c0 11 3 17 12 17s13-5 13-17M30 6c2-2 8-2 10 0" fill="none" stroke="#111" stroke-width="2.2"/><line x1="12" y1="9" x2="16" y2="15" stroke="#111"/><line x1="58" y1="9" x2="55" y2="15" stroke="#c0502a"/></svg>
    <div class="field" style="top:110px">Name</div>
    <div class="field" style="top:151px">Email</div>
    <div class="field" style="top:192px">Password</div>
    <div class="signup">Sign Up</div>
    <div class="terms">By clicking Sign Up button, you agree to our <a>Terms and Conditions</a>, and <a>Privacy Policy</a>.</div>
    <div class="signin">Already have an account? <b>SIGN IN.</b></div>
  </div>
</div>
</body>
</html>
```